Morning Mug sign

"Rise and Grind" is the catch phrase for this little Morning Mug.
This will be a two sided (printed on reflective alumaboard probably) sign that sits flat out on the ground in front of the store. We serve French Press and drip coffee to go.
The sign will be approx. 4' tall, and 2-3' wide.
One of the ideas for this sign is a hand coming out of the ground in front of a tombstone grasping a coffee cup..
there is a lot of room for designer discretion.
Early morning and in a rush crowd..
Store

```html
<!DOCTYPE html>
<html lang="en">
<head>
<meta charset="utf-8">
<title>Rise &amp; Grind – Sidewalk Sign</title>
<link href="https://fonts.googleapis.com/css2?family=Lobster&family=Lobster+Two:ital,wght@1,700&display=swap" rel="stylesheet">
<style>
  :root {
    --page-bg: #ececec;
    --burlap: #d6c796;
    --band: #380a06;
    --headline: #4a140e;
    --headline-edge: #ffffff;
    --tagline: #b5641f;
    --badge-fill: #f3e4c4;
    --badge-text: #c1362b;
    --beans: #6b3a1c;
    --beans-light: #9a5a2c;
    --steam: #f4f0ea;
  }
  * { margin: 0; padding: 0; box-sizing: border-box; }
  html, body { width: 1200px; height: 1000px; overflow: hidden; }
  body { background: var(--page-bg); position: relative; }

  .sign {
    position: absolute;
    left: 255px; top: 38px;
    width: 690px; height: 924px;
    background: var(--burlap);
    overflow: hidden;
  }
  .sign__band {
    position: absolute;
    left: 176px; top: 0;
    width: 342px; height: 100%;
    background: var(--band);
  }
  .brand {
    position: absolute;
    left: 44px; top: 48px;
    width: 150px; height: 150px;
    border-radius: 50%;
    background: var(--badge-fill);
    display: flex; align-items: center; justify-content: center;
    text-align: center;
  }
  .brand__name {
    font-family: "Lobster", cursive;
    font-size: 38px;
    line-height: 1.0;
    color: var(--badge-text);
  }
  .steam {
    position: absolute;
    left: 305px; top: 34px;
    width: 120px; height: 140px;
    border-radius: 50%;
    background: radial-gradient(circle, var(--steam) 0%, rgba(244,240,234,0.35) 70%, rgba(244,240,234,0) 100%);
  }
  .bean-cup {
    position: absolute;
    left: 216px; top: 200px;
    width: 250px; height: 200px;
    border-radius: 18px 18px 70px 70px;
    background: radial-gradient(ellipse at 55% 40%, var(--beans-light) 0%, var(--beans) 75%);
  }
  .headline {
    position: absolute;
    left: 176px; top: 400px;
    width: 342px;
    text-align: center;
    font-family: "Lobster", cursive;
    color: var(--headline);
    -webkit-text-stroke: 10px var(--headline-edge);
    paint-order: stroke fill;
    line-height: 1;
  }
  .headline__word { display: block; font-size: 118px; }
  .headline__amp { display: block; font-size: 72px; margin: -6px 0 -10px; }
  .tagline {
    position: absolute;
    left: 176px; top: 728px;
    width: 342px;
    text-align: center;
    font-family: "Lobster Two", cursive;
    font-style: italic;
    font-weight: 700;
    font-size: 40px;
    line-height: 52px;
    color: var(--tagline);
  }
</style>
</head>
<body>
  <main class="sign">
    <div class="sign__band"></div>

    <div class="brand"><span class="brand__name">Morning<br>Mug</span></div>

    <div class="steam" role="img" aria-label="White swirl of steam rising from the cup"></div>
    <div class="bean-cup" role="img" aria-label="Coffee cup shaped from roasted coffee beans"></div>

    <h1 class="headline">
      <span class="headline__word">Rise</span>
      <span class="headline__amp">&amp;</span>
      <span class="headline__word">Grind</span>
    </h1>

    <p class="tagline">Life Begins<br>Only<br>After Coffee</p>
  </main>
</body>
</html>
```